" Atendimento personalizado as necessidades do cliente em todos os ramos de tradução. Assistência 24h com plataforma online. Garantindo a segurança de toda documentação pela QTR, Pex, Velkor. "

```html
<!DOCTYPE html>
<html lang="pt-BR">
<head>
<meta charset="utf-8">
<title>LUMERA Traduções – Cartão de visita</title>
<link rel="stylesheet" href="https://fonts.googleapis.com/css2?family=Cinzel:wght@700&family=Open+Sans:wght@400;600&display=swap">
<style>
  :root {
    --stage: #2b2a29;
    --card-navy: #223759;
    --card-navy-deep: #1d3050;
    --accent-sky: #86c8f0;
    --accent-sky-soft: #6fb4e2;
    --text-white: #ffffff;
    --text-muted: #b9c6da;
  }
  * { box-sizing: border-box; margin: 0; padding: 0; }
  html, body {
    width: 1200px;
    height: 1200px;
    overflow: hidden;
    background: var(--stage);
  }
  .stage {
    width: 1200px;
    height: 1200px;
    display: flex;
    align-items: center;
    justify-content: center;
  }
  .business-card {
    position: relative;
    width: 1000px;
    height: 572px;
    background: linear-gradient(180deg, var(--card-navy) 0%, var(--card-navy-deep) 100%);
    overflow: hidden;
    font-family: "Open Sans", Arial, sans-serif;
    color: var(--text-white);
  }
  .brand {
    position: absolute;
    top: 150px;
    left: 0;
    right: 0;
    text-align: center;
  }
  .brand-name {
    font-family: "Cinzel", "Times New Roman", serif;
    font-weight: 700;
    font-size: 82px;
    letter-spacing: 2px;
    line-height: 1;
    color: var(--text-white);
  }
  .brand-tagline {
    margin-top: 6px;
    font-family: "Open Sans", Arial, sans-serif;
    font-size: 17px;
    letter-spacing: 14px;
    text-transform: uppercase;
    color: var(--text-muted);
  }
  .contact-row {
    position: absolute;
    top: 385px;
    left: 56px;
    right: 56px;
    display: flex;
    justify-content: space-between;
    align-items: flex-start;
  }
  .contact-item {
    display: flex;
    align-items: flex-start;
    gap: 12px;
    font-size: 17px;
    line-height: 1.35;
    color: var(--text-white);
  }
  .contact-icon {
    flex: none;
    width: 24px;
    height: 24px;
  }
  .contact-address { width: 270px; }
  .website {
    position: absolute;
    top: 468px;
    left: 56px;
    font-size: 24px;
    font-weight: 600;
    letter-spacing: 0.5px;
    color: var(--text-white);
  }
  .accent-band {
    position: absolute;
    left: 0;
    right: 0;
    bottom: 0;
    height: 22px;
    background: linear-gradient(180deg, var(--accent-sky-soft) 0%, var(--accent-sky) 100%);
  }
</style>
</head>
<body>
<main class="stage">
  <article class="business-card">
    <header class="brand">
      <div class="brand-name">LUMERA</div>
      <div class="brand-tagline">Traduções</div>
    </header>

    <section class="contact-row">
      <div class="contact-item contact-phone">
        <svg class="contact-icon" viewBox="0 0 24 24" aria-hidden="true">
          <circle cx="12" cy="12" r="12" fill="var(--accent-sky)"/>
          <path d="M8.2 6.5c.4-.3 1-.3 1.3.1l1.3 1.8c.3.4.2.9-.1 1.2l-.7.6c.5 1.2 1.6 2.4 2.9 3l.6-.7c.3-.4.9-.4 1.2-.1l1.8 1.3c.4.3.4.9.1 1.3l-.9 1c-.5.5-1.3.6-2 .3-2.9-1.3-5-3.5-6.2-6.3-.3-.7-.1-1.5.4-2z" fill="var(--card-navy)"/>
        </svg>
        <span>99 9 9999 99 99 | 9999 99 99</span>
      </div>

      <div class="contact-item contact-email">
        <svg class="contact-icon" viewBox="0 0 24 24" aria-hidden="true">
          <circle cx="12" cy="12" r="12" fill="var(--accent-sky)"/>
          <rect x="6" y="8" width="12" height="8.5" rx="1" fill="var(--card-navy)"/>
          <path d="M6.5 8.6 12 12.6l5.5-4" fill="none" stroke="var(--accent-sky)" stroke-width="1.2"/>
        </svg>
        <span>contato@lumera.com.br</span>
      </div>

      <div class="contact-item contact-address">
        <svg class="contact-icon" viewBox="0 0 24 24" aria-hidden="true">
          <circle cx="12" cy="12" r="12" fill="var(--accent-sky)"/>
          <path d="M12 5.5a4.2 4.2 0 0 0-4.2 4.2c0 3.1 4.2 8.3 4.2 8.3s4.2-5.2 4.2-8.3A4.2 4.2 0 0 0 12 5.5z" fill="var(--card-navy)"/>
          <circle cx="12" cy="9.7" r="1.6" fill="var(--accent-sky)"/>
        </svg>
        <span>Rua das Letras, 9999 | Centro<br>Sala 000 - CEP: 55.555-555<br>Cidade - UF</span>
      </div>
    </section>

    <div class="website">www.LUMERA.com.br</div>

    <div class="accent-band"></div>
  </article>
</main>
</body>
</html>
```